Qualvine.com needs a Mobile FIRST Site

Qualvine.com is an insurance broker based in Panama City, Panama that plans to sell car and motorcycle insurance online.

We need to design a total of 5 pages (two of those are A/B test pages). The site will be responsive and will be programmed in React. We will be using Bolt Kit´s library to code Qualvine.com. Keep in mind that we are using Bolt Kit to program the site´s functions, not to create the "look and feel" of the site, that is obviously your job. You can learn more about Bolt Kit here... https://boltkit.example/

We have created wireframes for the app. Please follow and keep in mind the instructions in the wireframes. You can change things here and there as long as the core functions and goals stay intact. We have uploaded the wireframes along with the company logo and color.

We are planning to A/B test the site´s home page so we need to design two homepages. You can find homepage A and B in the wireframes provided.

We speak Spanish in Panama but you can design the site in English. We can change the text once we receive the designs.

Target Market(s)

25-45 year olds who own a car or motorcylcle and own a credit card.

Industry/Entity Type

Insurance

Font styles to use
Sans Serif

Requirements
Must have
• Follow the wireframes provided and the logo colors.
Nice to have
• Please look at the Image I´ve uploaded from DeskHarbor, use it as reference to create HomePage A.

```html
<!DOCTYPE html>
<html lang="es">
<head>
<meta charset="utf-8">
<title>Qualvine.com – Claim Aquí</title>
<link rel="stylesheet" href="https://fonts.googleapis.com/css2?family=Poppins:wght@400;500;600;700&family=Open+Sans:wght@400;600&display=swap">
<style>
:root{
  --brand:#2d1a78;
  --brand-dark:#1d1150;
  --ink:#1a1a1a;
  --panel:#dedede;
  --ring:#dcdcdc;
  --bar:#a3a3a3;
  --white:#ffffff;
  --footer:#150d33;
}
*{box-sizing:border-box;margin:0;padding:0}
html,body{width:1200px;height:2209px;overflow:hidden;background:var(--white)}
.page{
  width:414px;height:762px;position:relative;
  transform:scale(2.89855);transform-origin:0 0;
  font-family:"Open Sans",Arial,sans-serif;color:var(--ink);
}
.brand{position:absolute;top:16px;left:0;width:414px;text-align:center;
  font-family:"Poppins",sans-serif;font-weight:700;font-size:29px;color:var(--brand);letter-spacing:-.5px}
.claim-title{position:absolute;top:63px;width:414px;text-align:center;
  font-family:"Poppins",sans-serif;font-weight:600;font-size:14px;color:#111}
.claim-text{position:absolute;top:84px;left:70px;width:274px;text-align:center;font-size:11px;line-height:16px;color:#222}

.steps{position:absolute;top:128px;left:0;width:414px;height:110px}
.step{position:absolute;width:80px;text-align:center}
.step svg{display:block;margin:0 auto}
.step-label{font-family:"Poppins",sans-serif;font-size:12.5px;color:#222;margin-top:2px}
.step-label.active{color:var(--brand)}

.tabs{position:absolute;top:254px;left:26px;width:362px;height:25px}
.tab{position:absolute;top:0;height:25px;display:flex;align-items:center;justify-content:center;gap:6px;
  font-family:"Poppins",sans-serif;font-size:15px}
.tab-motos{left:0;width:178px;background:var(--brand);color:var(--white)}
.tab-carros{left:185px;width:177px;background:var(--ring);color:var(--brand-dark)}

.plans{position:absolute;top:284px;left:26px;width:362px;height:432px;border:3px solid var(--brand);background:var(--panel)}
.plan{position:absolute;left:0;width:356px;height:207px}
.plan+.plan{border-top:3px solid var(--brand)}
.plan-photo{position:absolute;left:5px;top:3px;width:143px;height:119px}
.photo-black{background:radial-gradient(ellipse at 50% 55%,#3a3a3a 0%,#777 35%,#fff 70%)}
.photo-red{background:radial-gradient(ellipse at 50% 55%,#d21c22 0%,#e65a5e 35%,#fff 70%)}
.plan-price{position:absolute;left:5px;top:122px;width:143px;height:83px;text-align:center}
.price{font-family:"Poppins",sans-serif;font-weight:700;font-size:22px;color:var(--brand-dark);margin-top:12px;line-height:30px}
.buy{display:inline-block;margin-top:4px;width:80px;height:27px;border-radius:3px;background:var(--brand);
  color:var(--white);font-family:"Poppins",sans-serif;font-size:13px;line-height:27px}
.coverage{position:absolute;left:153px;top:3px;width:198px;height:119px;background:var(--white);padding:5px 5px 0}
.cov-label{font-size:10.5px;color:var(--brand);line-height:14px}
.cov-bar{width:142px;height:12px;border:1px solid #999;margin:2px 0 9px;background:var(--white)}
.cov-fill{height:100%;background:var(--bar);color:var(--white);font-size:8px;line-height:10px;padding-left:12px}
.benefits{position:absolute;left:153px;top:128px;width:198px;height:77px;background:var(--white);padding:5px 5px 0}
.ben-title{font-size:10.5px;color:var(--brand)}
.ben-list{display:flex;justify-content:space-between;margin-top:4px}
.ben{width:62px;text-align:center;font-size:8.5px;color:#111}
.ben svg{display:block;margin:0 auto 2px}

.footer{position:absolute;left:0;top:738px;width:414px;height:24px;background:var(--footer);
  color:var(--white);font-family:"Poppins",sans-serif;font-size:8px;line-height:24px;text-align:center}
</style>
</head>
<body>
<div class="page">
  <div class="brand">Qualvine.com</div>
  <h1 class="claim-title">CLAIM AQUÍ</h1>
  <p class="claim-text">Lorem ipsum dolor sit amet, consectetur lorem ipsum dolor sit amet, consecteturadipisicing elit, sed</p>

  <div class="steps">
    <div class="step" style="left:91px;top:0">
      <svg width="80" height="78" viewBox="0 0 80 78">
        <path d="M4 40 A36 36 0 0 0 76 40" fill="none" stroke="var(--ring)" stroke-width="10"/>
        <circle cx="40" cy="35" r="26" fill="var(--brand)"/>
        <circle cx="22" cy="15" r="8" fill="var(--white)" stroke="#222" stroke-width="1.5"/>
        <text x="22" y="19" font-family="Poppins" font-size="10" font-weight="600" text-anchor="middle" fill="#111">1</text>
        <path d="M38 30 l0 16 l4-4 l3 6 l2-1 l-3-6 l5 0 z" fill="none" stroke="#fff" stroke-width="1.4" stroke-linejoin="round"/>
        <path d="M34 26 a5 5 0 0 1 9 0" fill="none" stroke="#fff" stroke-width="1.2"/>
      </svg>
      <div class="step-label active">Elige</div>
    </div>
    <div class="step" style="left:167px;top:0">
      <svg width="80" height="78" viewBox="0 0 80 78">
        <path d="M4 38 A36 36 0 0 1 76 38" fill="none" stroke="var(--ring)" stroke-width="10"/>
        <circle cx="40" cy="35" r="26" fill="var(--white)" stroke="#fff"/>
        <path d="M31 22 h13 l6 6 v21 h-19 z M44 22 v6 h6" fill="none" stroke="#222" stroke-width="1.3"/>
        <path d="M35 32 h11 M35 36 h11 M35 40 h11 M35 44 h8" stroke="#222" stroke-width="1"/>
        <circle cx="40" cy="65" r="8" fill="var(--brand)"/>
        <text x="40" y="69" font-family="Poppins" font-size="10" font-weight="600" text-anchor="middle" fill="#fff">2</text>
      </svg>
      <div class="step-label">Datos</div>
    </div>
    <div class="step" style="left:251px;top:0">
      <svg width="80" height="78" viewBox="0 0 80 78">
        <path d="M4 40 A36 36 0 0 0 76 40" fill="none" stroke="var(--ring)" stroke-width="10"/>
        <circle cx="40" cy="35" r="25" fill="var(--white)" stroke="var(--brand)" stroke-width="1.5"/>
        <circle cx="40" cy="35" r="12" fill="none" stroke="#222" stroke-width="1.3"/>
        <circle cx="40" cy="35" r="9" fill="none" stroke="#222" stroke-width="1"/>
        <text x="40" y="39" font-family="Open Sans" font-size="11" text-anchor="middle" fill="#222">$</text>
        <circle cx="58" cy="15" r="8" fill="var(--brand)"/>
        <text x="58" y="19" font-family="Poppins" font-size="10" font-weight="600" text-anchor="middle" fill="#fff">3</text>
      </svg>
      <div class="step-label">Paga</div>
    </div>
  </div>

  <div class="tabs">
    <div class="tab tab-motos">
      <svg width="26" height="14" viewBox="0 0 26 14"><circle cx="5" cy="9" r="4" fill="none" stroke="#fff" stroke-width="1.8"/><circle cx="21" cy="9" r="4" fill="none" stroke="#fff" stroke-width="1.8"/><path d="M5 9 l6-5 h6 l4 5 M9 4 h5 M17 4 l-2-3 h3" fill="none" stroke="#fff" stroke-width="1.8"/></svg>
      Motos
    </div>
    <div class="tab tab-carros">
      <svg width="20" height="14" viewBox="0 0 20 14"><path d="M2 7 l2-5 h12 l2 5 v5 h-3 v-2 h-10 v2 h-3 z" fill="var(--brand-dark)"/><circle cx="5.5" cy="8" r="1.4" fill="var(--ring)"/><circle cx="14.5" cy="8" r="1.4" fill="var(--ring)"/><path d="M5 3.5 h10 l1 3 h-12 z" fill="var(--ring)"/></svg>
      Carros
    </div>
  </div>

  <div class="plans">
    <div class="plan" style="top:0">
      <div class="plan-photo photo-black" role="img" aria-label="Photo of a black sport motorcycle"></div>
      <div class="plan-price"><div class="price">$150.00</div><span class="buy">Comprar</span></div>
      <div class="coverage">
        <div class="cov-label">Insurance Coverage</div>
        <div class="cov-bar"><div class="cov-fill" style="width:60%">$ 10,000</div></div>
        <div class="cov-label">Insurance Coverage Limit By Accident</div>
        <div class="cov-bar"><div class="cov-fill" style="width:75%">$ 15,000</div></div>
        <div class="cov-label">Insurance Coverage By Year</div>
        <div class="cov-bar"><div class="cov-fill" style="width:93%">$ 17,000</div></div>
      </div>
      <div class="benefits">
        <div class="ben-title">Beneficios</div>
        <div class="ben-list">
          <div class="ben"><svg width="22" height="28" viewBox="0 0 22 28"><circle cx="11" cy="10" r="8" fill="none" stroke="var(--brand-dark)" stroke-width="1.3"/><path d="M11 6 l1.2 2.6 2.8.3-2.1 1.9.6 2.8-2.5-1.4-2.5 1.4.6-2.8-2.1-1.9 2.8-.3z" fill="none" stroke="var(--brand-dark)" stroke-width="1"/><path d="M6 16 l-2 10 4-2 2 3 1-8 M16 16 l2 10-4-2-2 3-1-8" fill="none" stroke="var(--brand-dark)" stroke-width="1.2"/></svg>Dolar Amet</div>
          <div class="ben"><svg width="28" height="28" viewBox="0 0 28 28"><path d="M3 12 h5 v13 h-5 z M8 13 l5-9 c2 0 3 1 2 4 l-1 3 h8 c2 0 3 2 2 3 l-2 9 c-.5 1.5-1.5 2-3 2 h-11" fill="none" stroke="var(--brand-dark)" stroke-width="1.3" stroke-linejoin="round"/></svg>Lorem Ipsum</div>
          <div class="ben"><svg width="24" height="28" viewBox="0 0 24 28"><path d="M8 4 h8 l-2 5 h-4 z M10 9 c-8 4-9 16 2 16 c11 0 10-12 2-16" fill="none" stroke="var(--brand-dark)" stroke-width="1.3"/><text x="12" y="21" font-family="Open Sans" font-size="9" text-anchor="middle" fill="var(--brand-dark)">$</text></svg>Constrectur</div>
        </div>
      </div>
    </div>

    <div class="plan" style="top:207px;height:219px">
      <div class="plan-photo photo-red" role="img" aria-label="Photo of a red sport motorcycle" style="top:5px"></div>
      <div class="plan-price" style="top:124px;height:88px"><div class="price" style="margin-top:14px">$120.00</div><span class="buy">Comprar</span></div>
      <div class="coverage" style="top:5px;height:119px">
        <div class="cov-label">Insurance Coverage</div>
        <div class="cov-bar"><div class="cov-fill" style="width:60%">$ 10,000</div></div>
        <div class="cov-label">Insurance Coverage Limit By Accident</div>
        <div class="cov-bar"><div class="cov-fill" style="width:75%">$ 15,000</div></div>
        <div class="cov-label">Insurance Coverage By Year</div>
        <div class="cov-bar"><div class="cov-fill" style="width:93%">$ 17,000</div></div>
      </div>
      <div class="benefits" style="top:128px;height:80px">
        <div class="ben-title">Beneficios</div>
        <div class="ben-list">
          <div class="ben"><svg width="22" height="28" viewBox="0 0 22 28"><circle cx="11" cy="10" r="8" fill="none" stroke="var(--brand-dark)" stroke-width="1.3"/><path d="M11 6 l1.2 2.6 2.8.3-2.1 1.9.6 2.8-2.5-1.4-2.5 1.4.6-2.8-2.1-1.9 2.8-.3z" fill="none" stroke="var(--brand-dark)" stroke-width="1"/><path d="M6 16 l-2 10 4-2 2 3 1-8 M16 16 l2 10-4-2-2 3-1-8" fill="none" stroke="var(--brand-dark)" stroke-width="1.2"/></svg>Dolar Amet</div>
          <div class="ben"><svg width="28" height="28" viewBox="0 0 28 28"><path d="M3 12 h5 v13 h-5 z M8 13 l5-9 c2 0 3 1 2 4 l-1 3 h8 c2 0 3 2 2 3 l-2 9 c-.5 1.5-1.5 2-3 2 h-11" fill="none" stroke="var(--brand-dark)" stroke-width="1.3" stroke-linejoin="round"/></svg>Lorem Ipsum</div>
          <div class="ben"><svg width="24" height="28" viewBox="0 0 24 28"><path d="M8 4 h8 l-2 5 h-4 z M10 9 c-8 4-9 16 2 16 c11 0 10-12 2-16" fill="none" stroke="var(--brand-dark)" stroke-width="1.3"/><text x="12" y="21" font-family="Open Sans" font-size="9" text-anchor="middle" fill="var(--brand-dark)">$</text></svg>Constrectur</div>
        </div>
      </div>
    </div>
  </div>

  <footer class="footer">Copyright © 2018, All Rights Reserved.</footer>
</div>
</body>
</html>
```